An our door sign really promoting our clinic and services

We have a new sports medicine clinic called HALLCREST SPORTS MEDICINE.
We want to make a really nice external sign at our clinic using a photo of our team we really like. I have attached the photo.
We want to simply include our LOGO and also signs with these slogan options. So we want different signs with these different slogans so we can choose what we really like.
This should be a simple and quite design.

The SLOGANS WE WOULD LIKE TO SEE ON THE SIGN (only one slogan per sign in the drafts)

1. Your Journey. Our Expertise
2. Where better health begins
3. Building the best version of you
4. Your health, in expert hands
5. Reaching new heights in your health
6. Your path to peak performance starts here

I have also included different versions of our logo based on the background and how you set the sign up

So summary
1. Image attached
2. Slogan options we would like to see them all
3. Logo attached (various options based on how you set the background up)
4. Size of sign is 2935mm wide x 1885mm high

```html
<!DOCTYPE html>
<html lang="en">
<head>
<meta charset="utf-8">
<title>Hallcrest Sports Medicine – Exterior Sign</title>
<link rel="stylesheet" href="https://fonts.googleapis.com/css2?family=Poppins:wght@800&family=Exo+2:wght@700&family=Great+Vibes&display=swap">
<style>
  :root {
    --backdrop: #b4b4b4;
    --navy-deep: #041a45;
    --navy: #0a2d6b;
    --navy-mid: #123c82;
    --cyan: #3ad2ff;
    --white: #ffffff;
  }
  * { margin: 0; padding: 0; box-sizing: border-box; }
  html, body {
    width: 1200px; height: 1098px; overflow: hidden;
    background: var(--backdrop);
  }
  .sign {
    position: absolute; left: 79px; top: 212px;
    width: 1046px; height: 672px; overflow: hidden;
    background: var(--navy-deep);
  }
  .gym-backdrop {
    position: absolute; inset: 0;
    background:
      radial-gradient(ellipse at 70% 40%, rgba(40,90,170,.55), transparent 60%),
      linear-gradient(100deg, var(--navy-deep) 0%, var(--navy) 45%, var(--navy-mid) 75%, #0c3170 100%);
  }
  .team-photo {
    position: absolute; left: 476px; top: 88px;
    width: 530px; height: 584px;
    background:
      radial-gradient(ellipse at 30% 35%, rgba(25,30,45,.85), transparent 55%),
      radial-gradient(ellipse at 78% 40%, rgba(30,40,70,.85), transparent 55%),
      linear-gradient(180deg, rgba(20,28,48,.2), rgba(15,20,35,.6));
    border-radius: 40% 40% 0 0 / 20% 20% 0 0;
  }
  .brand {
    position: absolute; left: 68px; top: 76px;
    display: flex; align-items: center; gap: 18px;
  }
  .brand-dot {
    width: 56px; height: 56px; border-radius: 50%;
    background: var(--cyan);
  }
  .brand-name {
    font-family: "Exo 2", sans-serif; font-weight: 700;
    color: var(--white); line-height: 1.05;
  }
  .brand-name .line-1 { display: block; font-size: 40px; letter-spacing: 1px; }
  .brand-name .line-2 { display: block; font-size: 19px; letter-spacing: 7.5px; }
  .headline {
    position: absolute; left: 62px; top: 192px;
    font-family: "Poppins", sans-serif; font-weight: 800;
  }
  .headline .lead {
    display: block; color: var(--white);
    font-size: 47px; letter-spacing: -1px; margin-left: 20px; line-height: 1;
  }
  .headline .big {
    display: block; color: var(--cyan);
    font-size: 152px; letter-spacing: -4px; line-height: 0.84;
    margin-top: 12px;
  }
  .headline .big .outline {
    color: transparent;
    -webkit-text-stroke: 1.5px var(--cyan);
  }
  .headline .script {
    display: block; color: var(--white);
    font-family: "Great Vibes", cursive; font-weight: 400;
    font-size: 120px; line-height: 1;
    margin: -30px 0 0 26px; letter-spacing: 0;
  }
</style>
</head>
<body>
  <main class="sign">
    <div class="gym-backdrop" role="img" aria-label="Clinic gym interior with training rig, tinted deep blue"></div>
    <div class="team-photo" role="img" aria-label="Team photo: a patient in black sportswear leaning on his knee beside a smiling practitioner in a navy polo holding a tablet"></div>

    <div class="brand">
      <span class="brand-dot"></span>
      <span class="brand-name">
        <span class="line-1">HALLCREST</span>
        <span class="line-2">SPORTS MEDICINE</span>
      </span>
    </div>

    <h1 class="headline">
      <span class="lead">BUILDING THE</span>
      <span class="big">BEST</span>
      <span class="big">VERSI<span class="outline">ON</span></span>
      <span class="script">of you</span>
    </h1>
  </main>
</body>
</html>
```